Young Entrepreneur needs the sexiest, slickest, hottest ANDROID ALARM APP DESIGN.

Now that I have your attention...

The name of the Application is BrimNote, using 'Stickers' this application is meant to get you to do what you need to do AND TO DO IT NOW, with a UI so simple my grandma can use it.

Using the provided sketches as a REFERENCE point, THREE (3) SCREENS will be needed, including a couple of design accents, which when the project is completed will be sent directly to a programming team.

Industry/Entity Type

Android

Requirements
Must have
• Creativity in simplicity. but please, go wild, do your 'thang'... Just keep it simple and clean.

```html
<!DOCTYPE html>
<html lang="en">
<head>
<meta charset="utf-8">
<title>BrimNote – Alarm Screen</title>
<link href="https://fonts.googleapis.com/css2?family=Open+Sans:wght@300;400;600&display=swap" rel="stylesheet">
<style>
  :root {
    --page-bg: #e9ecef;
    --sky-top: #a9dcf5;
    --sky-mid: #5fb6e6;
    --sky-bottom: #2a8fd2;
    --dial-face: #f4f8fb;
    --dial-edge: #d9e9f3;
    --time-blue: #2a86c8;
    --label-grey: #5f7d92;
    --text-light: #ffffff;
    --text-soft: rgba(255,255,255,0.85);
  }
  * { margin: 0; padding: 0; box-sizing: border-box; }
  html, body {
    width: 1200px; height: 900px; overflow: hidden;
    background: var(--page-bg);
    font-family: "Open Sans", sans-serif;
  }
  .alarm-screen {
    position: absolute;
    left: 330px; top: 30px;
    width: 540px; height: 840px;
    background:
      radial-gradient(circle at 50% 26%, rgba(255,255,255,0.35) 0, rgba(255,255,255,0) 42%),
      linear-gradient(180deg, var(--sky-top) 0%, var(--sky-mid) 45%, var(--sky-bottom) 100%);
    color: var(--text-light);
  }
  .weekday-row {
    display: flex; justify-content: space-between;
    padding: 26px 34px 0;
    list-style: none;
    font-size: 16px; font-weight: 400;
    color: var(--text-soft);
  }
  .alarm-dial {
    position: absolute;
    left: 50%; top: 100px;
    width: 250px; height: 250px;
    margin-left: -125px;
    border-radius: 50%;
    background: radial-gradient(circle at 50% 40%, #ffffff 0, var(--dial-face) 60%, var(--dial-edge) 100%);
    box-shadow: 0 0 0 6px rgba(255,255,255,0.35), 0 6px 24px rgba(20,90,140,0.18);
    display: flex; flex-direction: column; align-items: center; justify-content: center;
  }
  .alarm-time {
    position: relative;
    font-size: 92px; font-weight: 600; line-height: 1;
    color: var(--time-blue);
    letter-spacing: -1px;
    margin-top: -8px;
  }
  .alarm-meridiem {
    position: absolute;
    right: -28px; top: -6px;
    font-size: 20px; font-weight: 400;
    color: var(--time-blue);
  }
  .alarm-label {
    font-size: 34px; font-weight: 400;
    color: var(--label-grey);
    margin-top: 8px;
  }
  .alarm-actions {
    position: absolute;
    left: 0; right: 0; top: 430px;
    list-style: none; text-align: center;
    font-size: 19px; font-weight: 300;
    line-height: 38px;
    color: var(--text-soft);
  }
  .brand-mark {
    position: absolute;
    left: 0; right: 0; bottom: 48px;
    display: flex; align-items: center; justify-content: center; gap: 10px;
    font-size: 22px; font-weight: 600;
    color: var(--text-light);
  }
  .brand-dot {
    width: 12px; height: 12px; border-radius: 50%;
    background: var(--text-light);
  }
</style>
</head>
<body>
  <main class="alarm-screen">
    <ul class="weekday-row">
      <li>Mon</li><li>Tue</li><li>Wed</li><li>Thu</li><li>Fri</li><li>Sat</li><li>Sun</li>
    </ul>

    <div class="alarm-dial">
      <div class="alarm-time">6:40<span class="alarm-meridiem">am</span></div>
      <div class="alarm-label">Shower</div>
    </div>

    <ul class="alarm-actions">
      <li>On/Off</li>
      <li>Delete</li>
      <li>Sounds</li>
      <li>Color</li>
      <li>Set Sticky</li>
      <li>Save</li>
    </ul>

    <div class="brand-mark"><span class="brand-dot"></span>BrimNote</div>
  </main>
</body>
</html>
```